The Quiet Harbour Cafe / Bar & Restaurant *

needs a signage design for the restaurant an...

We are opening a Cafe Bar Restaurant in Thailand and require signage made for outside the restaurant to welcome the customers into the restaurant.
Also a design for the Menu selling Thai & Western Food.

```html
<!DOCTYPE html>
<html lang="en">
<head>
<meta charset="utf-8">
<title>The Quiet Harbour Cafe – Welcome Sign</title>
<link rel="stylesheet" href="https://fonts.googleapis.com/css2?family=Bebas+Neue&display=swap">
<style>
  :root {
    --backdrop-inner: #5b5b5c;
    --backdrop-outer: #3a3a3b;
    --sign-light: #f2f2f2;
    --sign-shade: #e4e4e4;
    --brand-red: #8b1019;
    --brand-green: #a6ce39;
  }
  * { margin: 0; padding: 0; box-sizing: border-box; }
  html, body { width: 1200px; height: 999px; overflow: hidden; }
  body {
    background: radial-gradient(ellipse at 50% 45%, var(--backdrop-inner) 0%, var(--backdrop-outer) 80%);
    position: relative;
    font-family: "Bebas Neue", "Oswald", sans-serif;
  }
  .welcome-sign {
    position: absolute;
    left: 36px; top: 233px;
    width: 1128px; height: 533px;
    background: linear-gradient(180deg, var(--sign-light) 0%, var(--sign-shade) 100%);
    overflow: hidden;
  }
  .food-band { position: absolute; inset: 0; width: 1128px; height: 533px; }
  .sign-heading {
    position: absolute;
    left: 644px; top: 26px;
    font-size: 116px; line-height: 1;
    color: var(--brand-red);
    font-weight: 400;
    letter-spacing: 1px;
  }
  .venue-name {
    position: absolute;
    left: 18px; top: 384px;
    font-size: 57px; line-height: 1;
    color: var(--brand-red);
    font-weight: 400;
  }
  .venue-type {
    position: absolute;
    left: 25px; top: 444px;
    font-size: 57px; line-height: 1;
    color: var(--brand-green);
    font-weight: 400;
  }
</style>
</head>
<body>
  <section class="welcome-sign">
    <svg class="food-band" viewBox="0 0 1128 533" xmlns="http://www.w3.org/2000/svg">
      <defs>
        <clipPath id="wave-window">
          <path d="M0,45 C250,28 420,90 560,140 C700,190 900,192 1128,85 L1128,392 C950,500 760,490 600,420 C400,330 150,300 0,345 Z"/>
        </clipPath>
        <linearGradient id="tone-soup" x1="0" y1="0" x2="0" y2="1">
          <stop offset="0" stop-color="#6b4a32"/><stop offset="0.45" stop-color="#e9a24a"/><stop offset="1" stop-color="#f4f1ea"/>
        </linearGradient>
        <linearGradient id="tone-fried" x1="0" y1="0" x2="1" y2="1">
          <stop offset="0" stop-color="#c0392b"/><stop offset="0.5" stop-color="#8a4e22"/><stop offset="1" stop-color="#5e3716"/>
        </linearGradient>
        <linearGradient id="tone-greens" x1="0" y1="0" x2="1" y2="1">
          <stop offset="0" stop-color="#7fb94a"/><stop offset="0.5" stop-color="#eef2e6"/><stop offset="1" stop-color="#9bc66a"/>
        </linearGradient>
        <linearGradient id="tone-plate" x1="0" y1="0" x2="0" y2="1">
          <stop offset="0" stop-color="#2a2a2a"/><stop offset="0.5" stop-color="#a07a52"/><stop offset="1" stop-color="#2e2e2e"/>
        </linearGradient>
        <linearGradient id="tone-salad" x1="0" y1="0" x2="0" y2="1">
          <stop offset="0" stop-color="#d96a3c"/><stop offset="0.5" stop-color="#5f8f3a"/><stop offset="1" stop-color="#c9c3b6"/>
        </linearGradient>
      </defs>
      <g clip-path="url(#wave-window)">
        <rect x="0" y="0" width="246" height="533" fill="url(#tone-soup)" role="img" aria-label="Photo of prawn soup in a white bowl with lime and herbs"/>
        <rect x="246" y="0" width="254" height="533" fill="url(#tone-fried)" role="img" aria-label="Photo of crispy fried dish topped with sliced chilli and shallots"/>
        <rect x="500" y="0" width="250" height="533" fill="url(#tone-greens)" role="img" aria-label="Photo of lettuce, cucumber and chilli garnish on a white plate"/>
        <rect x="750" y="0" width="249" height="533" fill="url(#tone-plate)" role="img" aria-label="Photo of a spicy noodle salad on a square white plate"/>
        <rect x="999" y="0" width="129" height="533" fill="url(#tone-salad)" role="img" aria-label="Photo of a fresh seafood salad with herbs"/>
        <g stroke="var(--brand-green)" stroke-width="6">
          <line x1="246" y1="0" x2="246" y2="533"/>
          <line x1="500" y1="0" x2="500" y2="533"/>
          <line x1="750" y1="0" x2="750" y2="533"/>
          <line x1="999" y1="0" x2="999" y2="533"/>
        </g>
      </g>
      <g fill="none" stroke="var(--brand-green)" stroke-width="6">
        <path d="M0,45 C250,28 420,90 560,140 C700,190 900,192 1128,85"/>
        <path d="M0,345 C150,300 400,330 600,420 C760,490 950,500 1128,392"/>
      </g>
    </svg>
    <h1 class="sign-heading">WELCOME</h1>
    <p class="venue-name">THE QUIET HARBOUR CAFE</p>
    <p class="venue-type">BAR &amp; RESTAURANT</p>
  </section>
</body>
</html>
```